Ferrant Valley Zoning Council Business Cards

We're looking for a business card design, simple as that. We're a local government agency that mainly performs building code enforcement, transportation planning, floodplain management, and GIS for Tobelle Parish in Louisiana, and other surround parishes. So you're not having to Google anything, GIS is, at it's core, mapping. Building Code Enforcement is just that, nothing more. Floodplain Management is to make sure the public is within what the government

Contact Information for Business Card

Our Address is

517 Marwick Street
Alexandria, LA 71489

Our phone is 3185529137
Our fax is 3185529142
Our website is www.fvzc.info
My email is dana@fvzc.info

Font styles to use
Serif
Sans Serif

Colors

Designer to choose colors to be used in the design.

Requirements
Must have
• I'm attaching our logo(several versions) that must be incorporated. The design should fit well with our existing logo. I can send photoshop files for our logo if needed. If possible, I'd like to be able to add names/info to each card for all of our employees once this is done.
Nice to have
• The Louisiana state seal is a bonus, and isn't specifically required.

```html
<!DOCTYPE html>
<html lang="en">
<head>
<meta charset="utf-8">
<title>Ferrant Valley Zoning Council – Business Cards</title>
<link rel="stylesheet" href="https://fonts.googleapis.com/css2?family=Montserrat:wght@300;700&family=Open+Sans:wght@400;600&display=swap">
<style>
  :root {
    --page: #d9d9d9;
    --card: #1d1d1d;
    --card-edge: #141414;
    --map-tone: #2b2b2b;
    --white: #f4f4f4;
    --muted: #8a8a8a;
    --blue: #3b51b0;
    --green: #2fa14a;
    --orange: #e8921e;
    --lime: #b9cf1c;
    --seal-blue: #1f3e8c;
  }
  * { box-sizing: border-box; margin: 0; padding: 0; }
  html, body { width: 1200px; height: 1021px; overflow: hidden; background: var(--page); }
  body { position: relative; font-family: "Open Sans", sans-serif; color: var(--white); }

  .card {
    position: absolute;
    width: 760px; height: 434px;
    background: var(--card);
    border: 1px solid var(--card-edge);
    box-shadow: 0 14px 30px rgba(0,0,0,.28);
    overflow: hidden;
  }
  .card--front { left: 300px; top: 58px; }
  .card--back  { left: 140px; top: 530px; }

  /* front */
  .state-map {
    position: absolute; left: 150px; top: 40px;
    width: 320px; height: 260px;
    background: linear-gradient(160deg, var(--map-tone), #242424);
    border-radius: 4px;
  }
  .wordmark { position: absolute; font-family: "Montserrat", sans-serif; font-weight: 700; color: var(--white); line-height: 1; letter-spacing: 2px; }
  .wordmark-sub { position: absolute; font-family: "Montserrat", sans-serif; font-weight: 300; color: var(--muted); letter-spacing: .5px; }
  .card--front .wordmark { left: 80px; top: 200px; font-size: 112px; }
  .card--front .wordmark-sub { left: 82px; top: 316px; font-size: 16px; }
  .brand-dot { position: absolute; border-radius: 50%; background: var(--green); }
  .card--front .brand-dot { left: 540px; top: 150px; width: 150px; height: 150px; }

  /* back */
  .card--back .brand-dot { left: 56px; top: 50px; width: 58px; height: 58px; }
  .card--back .wordmark { left: 128px; top: 48px; font-size: 70px; }
  .card--back .wordmark-sub { left: 130px; top: 120px; font-size: 11px; }

  .person-name { position: absolute; left: 60px; top: 168px; font-size: 27px; font-weight: 600; color: var(--blue); }
  .person-title { position: absolute; left: 60px; top: 204px; font-size: 19px; }
  .rule { position: absolute; left: 60px; top: 250px; width: 56px; height: 2px; background: var(--green); }

  .address { position: absolute; left: 60px; top: 292px; font-size: 19px; line-height: 1.35; }
  .contact { position: absolute; font-size: 19px; line-height: 1.4; list-style: none; }
  .contact li { display: flex; align-items: center; gap: 8px; }
  .contact svg { width: 17px; height: 17px; fill: var(--orange); flex: none; }
  .contact--phone { left: 320px; top: 318px; }
  .contact--web { left: 520px; top: 338px; }

  .seal {
    position: absolute; left: 592px; top: 120px;
    width: 108px; height: 108px; border-radius: 50%;
    background: var(--white);
    border: 4px solid var(--seal-blue);
    box-shadow: inset 0 0 0 14px var(--white), inset 0 0 0 60px var(--seal-blue);
  }
</style>
</head>
<body>

<section class="card card--front" aria-label="Card front">
  <div class="state-map" role="img" aria-label="Faint silhouette map of Louisiana"></div>
  <div class="wordmark">FVZC</div>
  <div class="wordmark-sub">Ferrant Valley Zoning Council</div>
  <div class="brand-dot" aria-hidden="true"></div>
</section>

<section class="card card--back" aria-label="Card back">
  <div class="brand-dot" aria-hidden="true"></div>
  <div class="wordmark">FVZC</div>
  <div class="wordmark-sub">Ferrant Valley Zoning Council</div>

  <div class="person-name">Caleb Ardent</div>
  <div class="person-title">Founder</div>
  <div class="rule"></div>

  <address class="address" style="font-style:normal">517 Marwick Street<br>Alexandria, LA 71489</address>

  <ul class="contact contact--phone">
    <li><svg viewBox="0 0 24 24" aria-label="Phone"><path d="M6.6 10.8a15.1 15.1 0 0 0 6.6 6.6l2.2-2.2c.3-.3.7-.4 1-.2 1.1.4 2.3.6 3.6.6.6 0 1 .4 1 1V20c0 .6-.4 1-1 1A17 17 0 0 1 3 4c0-.6.4-1 1-1h3.5c.6 0 1 .4 1 1 0 1.3.2 2.5.6 3.6.1.3 0 .7-.2 1z"/></svg>318-552-9137</li>
    <li><svg viewBox="0 0 24 24" aria-label="Fax"><path d="M7 3h10v5H7zM4 9h16a2 2 0 0 1 2 2v6h-4v4H6v-4H2v-6a2 2 0 0 1 2-2zm4 7v3h8v-3z"/></svg>318-552-9142</li>
  </ul>

  <ul class="contact contact--web">
    <li><svg viewBox="0 0 24 24" aria-label="Email"><path d="M2 5h20v14H2zm2 2v.5l8 5 8-5V7zm0 2.8V17h16V9.8l-8 5z"/></svg>dana@fvzc.info</li>
    <li><svg viewBox="0 0 24 24" aria-label="Website"><path d="M12 2a10 10 0 1 0 0 20 10 10 0 0 0 0-20zm0 2c.9 1.2 1.6 2.6 2 4h-4c.4-1.4 1.1-2.8 2-4zM4.3 14a8 8 0 0 1 0-4h3.4a16 16 0 0 0 0 4zm.8 2h3c.4 1.3.9 2.5 1.6 3.6A8 8 0 0 1 5.1 16zm3-8h-3a8 8 0 0 1 4.6-3.6C9 5.5 8.5 6.7 8.1 8zM12 20c-.9-1.2-1.6-2.6-2-4h4c-.4 1.4-1.1 2.8-2 4zm2.3-6H9.7a14 14 0 0 1 0-4h4.6a14 14 0 0 1 0 4zm.1 5.6c.7-1.1 1.2-2.3 1.6-3.6h3a8 8 0 0 1-4.6 3.6zm1.9-5.6a16 16 0 0 0 0-4h3.4a8 8 0 0 1 0 4zm-.3-6c-.4-1.3-.9-2.5-1.6-3.6A8 8 0 0 1 18.9 8z"/></svg>www.fvzc.info</li>
  </ul>

  <div class="seal" role="img" aria-label="State seal badge"></div>
</section>

</body>
</html>
```